Website for new dental office

I am Dr. Colin Marsh and am building a new dental practice. I specialize in general dentistry. I am young and have a higher end dental practice incorporating very new technologies and would like my website to reflect that. As many dental patients are older, the website must be very easy to navigate. I would like patients to be able to request appointments, and will eventually add on patient information forms (the health history, etc, that you normally fill out in the practice) from my practice management software, so leave an area for that.

Industry/Entity Type

Building

```html
<!DOCTYPE html>
<html lang="en">
<head>
<meta charset="utf-8">
<title>Colin Marsh, DDS</title>
<link href="https://fonts.googleapis.com/css2?family=Lato:wght@400;700&family=Open+Sans:ital,wght@0,400;0,600;0,700;1,400&display=swap" rel="stylesheet">
<style>
:root{
  --page:#efefef;
  --white:#ffffff;
  --ink:#2b2b2b;
  --body-text:#555555;
  --blue:#6a87d0;
  --blue-deep:#4a68b8;
  --blue-line:#2f5bb7;
  --dark:#333333;
  --green-top:#b4dc43;
  --green-bottom:#8cc21d;
  --orange-top:#ffa43a;
  --orange-bottom:#f58220;
  --border:#dddddd;
  --dots:#bdbdbd;
}
*{box-sizing:border-box;margin:0;padding:0}
h1,h2,h3{font-weight:400}
html,body{width:958px;height:1200px;overflow:hidden}
body{background:var(--page);font-family:"Open Sans",Arial,sans-serif;color:var(--ink)}
.page{position:relative;width:958px;height:1200px}
.abs{position:absolute}

/* header */
.brand{left:86px;top:38px;font-family:"Lato",sans-serif;font-size:28px;font-weight:400;color:var(--ink);white-space:nowrap}
.consult-btn{left:654px;top:12px;width:216px;height:34px;border-radius:3px;background:linear-gradient(var(--green-top),var(--green-bottom));display:flex;align-items:center;justify-content:center;gap:8px;font-size:12px;font-weight:700;color:#1e2a06}
.header-rule{left:654px;top:58px;width:216px;height:1px;background:#dcdcdc}
.phone{right:90px;top:64px;display:flex;align-items:center;gap:5px;font-size:16px;color:var(--ink)}

/* nav */
.main-nav{left:88px;top:100px;width:782px;height:30px;background:var(--blue);display:flex;list-style:none}
.main-nav li{display:flex;align-items:center;justify-content:center;color:var(--white);font-size:11px;font-family:"Open Sans",sans-serif}
.main-nav li.active{background:var(--dark);width:60px;font-weight:700}
.main-nav li.item{flex:1}
.main-nav li.wide{flex:1.5}

/* hero */
.hero{left:88px;top:138px;width:782px;height:284px;border:1px solid var(--border);border-radius:3px;overflow:hidden;background:linear-gradient(90deg,#f4f4f4 0%,#e9ebec 45%,#dfe3e6 62%,#d3d8dc 80%,#e6eaec 100%)}
.hero-title{left:0;top:100px;height:42px;width:331px;background:#222;border-radius:0 3px 3px 0;color:var(--white);font-family:"Lato",sans-serif;font-weight:700;font-size:21px;display:flex;align-items:center;padding-left:12px;white-space:nowrap}
.hero-sub{left:0;top:146px;height:30px;width:277px;background:#3a3a3a;border-radius:0 3px 3px 0;color:var(--white);font-family:"Lato",sans-serif;font-size:14px;display:flex;align-items:center;padding-left:12px;white-space:nowrap}

/* appointment */
.appt{left:88px;top:433px;width:782px;height:67px;background:var(--blue);border-left:8px solid #222}
.appt-title{left:105px;top:459px;color:var(--white);font-size:13px;font-weight:400;white-space:nowrap}
.field{width:178px;height:21px;background:#f7f7f7;border:1px solid #d4d4d4;font-size:8px;color:#8a8a8a;display:flex;align-items:center;padding-left:10px}
.appt-btn{left:657px;top:470px;width:186px;height:24px;border-radius:2px;background:linear-gradient(var(--orange-top),var(--orange-bottom));color:var(--white);font-size:12px;font-weight:700;display:flex;align-items:center;justify-content:center;gap:6px;border:1px solid #e07010;white-space:nowrap}

/* tabs */
.tab{top:525px;height:34px;border:1px solid var(--border);border-bottom:none;border-radius:3px 3px 0 0;background:#f5f5f5;color:#8a8a8a;font-size:12.5px;display:flex;align-items:center;justify-content:center}
.tab.active{background:var(--white);border-top:3px solid var(--blue-deep);color:var(--blue-deep);height:35px}
.panel{left:88px;top:558px;width:782px;height:230px;background:var(--white);border:1px solid #e4e4e4}
.welcome-photo{left:106px;top:584px;width:281px;height:172px;border:3px solid #eeeeee;background:linear-gradient(120deg,#c9d3e6 0%,#e9e4df 35%,#b7c8d8 60%,#eef2f6 100%)}
.welcome-title{left:402px;top:581px;font-family:"Lato",sans-serif;font-size:19px;font-weight:400;color:#222;white-space:nowrap}
.welcome-text{left:404px;top:616px;width:452px;font-family:"Open Sans",sans-serif;font-size:9.4px;line-height:15.2px;color:var(--body-text)}
.read-btn{left:402px;top:733px;width:97px;height:30px;background:var(--dark);color:var(--white);font-size:11px;display:flex;align-items:center;justify-content:center}

/* lower */
.lower{left:87px;top:808px;width:782px;height:354px;background:var(--white);box-shadow:0 0 18px rgba(0,0,0,.12)}
.section-title{font-size:19px;font-weight:400;color:var(--blue-deep);white-space:nowrap}
.rule-thick{height:3px;background:var(--blue-deep)}
.rule-dots{height:0;border-top:1px dotted var(--dots)}
.case-photo{height:102px}
.case-title{font-size:14px;font-weight:400;color:#222}
.case-text{font-size:9.4px;line-height:12.8px;color:#666;width:226px}
.case-rule{height:1px;background:#d6d6d6;width:222px}
.read-more{font-size:9px;font-style:italic;color:#555;display:flex;align-items:center;gap:8px}
.read-more .box{width:10px;height:10px;background:#333;display:flex;align-items:center;justify-content:center}

.testi-title{left:598px;top:838px;font-size:15px;font-weight:400;color:var(--blue-deep)}
.arrow-btn{top:843px;width:14px;height:13px;background:#eeeeee;display:flex;align-items:center;justify-content:center}
.testi-box{left:598px;top:878px;width:240px;height:151px;border:1px solid #dcdcdc}
.testi-text{left:614px;top:892px;width:200px;font-size:9.4px;line-height:14.4px;color:#666}
.testi-name{left:695px;top:952px;font-size:12px;font-weight:700;color:#111}
.avatar-ring{left:614px;top:976px;width:80px;height:80px;border-radius:50%;background:var(--white);border:1px solid #e2e2e2;display:flex;align-items:center;justify-content:center}
.avatar{width:64px;height:64px;border-radius:50%;background:radial-gradient(circle at 50% 40%,#5a4a44,#1c1c1c)}
.schedule{left:599px;top:1077px;width:240px;height:66px;border-radius:2px;background:linear-gradient(var(--orange-top),var(--orange-bottom));color:var(--white)}
.schedule h3{position:absolute;left:9px;top:8px;font-size:14.5px;font-weight:600;white-space:nowrap}
.schedule p{position:absolute;left:9px;top:33px;width:175px;font-size:9px;line-height:12px}
.footer{left:0;top:1176px;width:976px;text-align:center;font-family:"Lato",sans-serif;font-size:10.5px;color:#333}
</style>
</head>
<body>
<div class="page">

  <header>
    <div class="abs brand">Colin Marsh, DDS</div>
    <div class="abs consult-btn">
      <svg width="14" height="12" viewBox="0 0 14 12"><rect x="1" y="3" width="12" height="8" rx="1" fill="none" stroke="#1e2a06" stroke-width="1.3"/><path d="M5 3V1h4v2" fill="none" stroke="#1e2a06" stroke-width="1.3"/></svg>
      Request a FREE Consultation
    </div>
    <div class="abs header-rule"></div>
    <div class="abs phone">
      <svg width="24" height="22" viewBox="0 0 24 22"><ellipse cx="14" cy="7" rx="8" ry="5.5" fill="none" stroke="#222" stroke-width="1.4"/><circle cx="11" cy="7" r="1" fill="#222"/><circle cx="14" cy="7" r="1" fill="#222"/><circle cx="17" cy="7" r="1" fill="#222"/><path d="M3 8c-2 4 2 10 7 12l2-3-3-2-1 1c-2-1-3-3-3-5l1-1-1-3z" fill="#222"/></svg>
      (555) 0142-377
    </div>
  </header>

  <ul class="abs main-nav">
    <li class="active">HOME</li>
    <li class="item">Our Team</li>
    <li class="item">Philosophy</li>
    <li class="item">Restorative</li>
    <li class="item">Cosmetic</li>
    <li class="wide">Tooth Replacement</li>
    <li class="item">First Visit</li>
    <li class="item">Contact</li>
  </ul>

  <section class="abs hero" role="img" aria-label="Smiling young dentist in a white coat standing in a bright modern treatment room">
    <div class="abs hero-title">I specialize in general dentistry</div>
    <div class="abs hero-sub">Teeth Whitening Solutions for Everyone</div>
  </section>

  <section>
    <div class="abs appt"></div>
    <div class="abs appt-title">REQUEST AN APPOINTMENT</div>
    <div class="abs field" style="left:288px;top:442px">Your Name</div>
    <div class="abs field" style="left:473px;top:442px">Preferred date</div>
    <div class="abs field" style="left:657px;top:442px;width:186px">Preferred day</div>
    <div class="abs field" style="left:288px;top:471px">Your Email</div>
    <div class="abs field" style="left:473px;top:471px">Phone number</div>
    <div class="abs appt-btn">REQUEST AN APPOINTMENT
      <svg width="10" height="10" viewBox="0 0 10 10"><path d="M1 1l4 4-4 4M5 1l4 4-4 4" fill="none" stroke="#fff" stroke-width="1.6"/></svg>
    </div>
  </section>

  <section>
    <div class="abs panel"></div>
    <div class="abs tab active" style="left:102px;width:106px">Our Team</div>
    <div class="abs tab" style="left:216px;width:104px">Patient Stories</div>
    <div class="abs tab" style="left:330px;width:104px">health history</div>
    <div class="abs welcome-photo" role="img" aria-label="Dentist examining a smiling patient in the treatment chair"></div>
    <h2 class="abs welcome-title">Welcome to Colin Marsh, DDS</h2>
    <p class="abs welcome-text">It is a long established fact that a reader will be distracted by the readable content of a page when looking at its layout. The point of using Lorem Ipsum is that it has a more-or-less normal distribution of letters, as opposed to using 'Content here, content here', making it look like readable English. Many desktop publishing packages and web page editors now use Lorem Ipsum as their default model text, and a search for 'lorem ipsum' will uncover many web sites still in their infancy. Various versions have evolved over the years, sometimes by accident, sometimes on purpose (injected humour and the like).</p>
    <div class="abs read-btn">READ MORE</div>
  </section>

  <section>
    <div class="abs lower"></div>

    <h2 class="abs section-title" style="left:98px;top:834px">Case Studies</h2>
    <div class="abs rule-thick" style="left:218px;top:848px;width:92px"></div>
    <div class="abs rule-dots" style="left:310px;top:849px;width:254px"></div>

    <div class="abs case-photo" style="left:104px;top:878px;width:216px;background:linear-gradient(180deg,#f0d8cc,#c9473f 55%,#f2ddd3)" role="img" aria-label="Close-up of a bright white smile"></div>
    <h3 class="abs case-title" style="left:100px;top:987px">Cosmetics</h3>
    <div class="abs rule-dots" style="left:100px;top:1008px;width:220px"></div>
    <p class="abs case-text" style="left:100px;top:1021px">Lorem Ipsum is simply dummy text of the printing and typesetting industry. Lorem Ipsum has been the industry's standard dummy text ever since the 1500s,</p>
    <div class="abs case-rule" style="left:98px;top:1106px"></div>
    <div class="abs read-more" style="left:99px;top:1115px">Read more <span class="box"><svg width="5" height="6" viewBox="0 0 5 6"><path d="M1 0l3 3-3 3" fill="none" stroke="#fff"/></svg></span></div>

    <div class="abs case-photo" style="left:342px;top:878px;width:220px;background:linear-gradient(90deg,#e7d4cc,#f2e6e2 50%,#d7a9a4)" role="img" aria-label="Patient having teeth checked with a dental mirror"></div>
    <h3 class="abs case-title" style="left:342px;top:987px">Restorative</h3>
    <div class="abs rule-dots" style="left:342px;top:1008px;width:222px"></div>
    <p class="abs case-text" style="left:345px;top:1021px">Lorem Ipsum is simply dummy text of the printing and typesetting industry. Lorem Ipsum has been the industry's standard dummy text ever since the 1500s,</p>
    <div class="abs case-rule" style="left:337px;top:1106px"></div>
    <div class="abs read-more" style="left:340px;top:1115px">Read more <span class="box"><svg width="5" height="6" viewBox="0 0 5 6"><path d="M1 0l3 3-3 3" fill="none" stroke="#fff"/></svg></span></div>

    <h2 class="abs testi-title">Testimonials</h2>
    <div class="abs" style="left:706px;top:848px;width:54px;height:3px;background:var(--blue-line)"></div>
    <div class="abs rule-dots" style="left:760px;top:849px;width:52px"></div>
    <div class="abs arrow-btn" style="left:821px"><svg width="4" height="6" viewBox="0 0 4 6"><path d="M3 0L0 3l3 3" fill="none" stroke="#aaa"/></svg></div>
    <div class="abs arrow-btn" style="left:837px"><svg width="4" height="6" viewBox="0 0 4 6"><path d="M1 0l3 3-3 3" fill="none" stroke="#aaa"/></svg></div>

    <div class="abs testi-box"></div>
    <p class="abs testi-text">Lorem ipsum dolor slo onsec nelioro tue raliquet Morbi nec In Curabitur, lorem in design Morbi nec In Curabitur lreaoreet nisl</p>
    <svg class="abs" style="left:777px;top:944px" width="40" height="32" viewBox="0 0 40 32"><path d="M2 0h14v14l-6 18H4l5-16H2z M22 0h14v14l-6 18h-6l5-16h-7z" fill="#ececec"/></svg>
    <div class="abs testi-name">Daniel Hart</div>
    <div class="abs avatar-ring"><div class="avatar" role="img" aria-label="Portrait of the patient giving the testimonial"></div></div>

    <div class="abs schedule">
      <h3>Schedule Your Appointment</h3>
      <p>Lorem Ipsum is simply dummy text of the printing and typesetting industry.</p>
      <svg class="abs" style="left:193px;top:27px" width="32" height="30" viewBox="0 0 32 30"><rect x="2" y="4" width="28" height="24" rx="2" fill="none" stroke="#3a2a1a" stroke-width="2"/><line x1="2" y1="10" x2="30" y2="10" stroke="#3a2a1a" stroke-width="2"/><line x1="9" y1="1" x2="9" y2="7" stroke="#3a2a1a" stroke-width="2"/><line x1="23" y1="1" x2="23" y2="7" stroke="#3a2a1a" stroke-width="2"/><g fill="#3a2a1a"><rect x="7" y="13" width="4" height="3"/><rect x="14" y="13" width="4" height="3"/><rect x="21" y="13" width="4" height="3"/><rect x="7" y="19" width="4" height="3"/><rect x="14" y="19" width="4" height="3"/><rect x="21" y="19" width="4" height="3"/></g></svg>
    </div>
  </section>

  <footer class="abs footer">© Copyrights 2014 All rights Reserved</footer>
</div>
</body>
</html>
```